Storage Auctions Book Cover

I need a new cover for my book which is located here:
http://www.brellomart.example/dp/Q7TX2PLM4R/
The book is about making money by buying storage units at auction, made popular by the reality shows "Locker Raiders" and "Bid Trackers." It's for entrepreneurs and those looking for a weekend business.
The current cover was homemade in Gimp, and it's holding back sales. I think it needs a better cover in order to look more professional and catch more attention.
Updates
So far, I really like the designs from Pumbleford and voskworks. Consider those two what I'm looking for, they are both good.

```html
<!DOCTYPE html>
<html lang="en">
<head>
<meta charset="utf-8">
<title>Making Money in Storage Auctions – Book Cover</title>
<link rel="stylesheet" href="https://fonts.googleapis.com/css2?family=Archivo+Black&family=Anton&family=Fjalla+One&display=swap">
<style>
  :root {
    --door-orange: #e98a2c;
    --door-light: #f29a3c;
    --door-shadow: #b9611a;
    --door-deep: #9c4f12;
    --ink: #2a1608;
    --title-white: #f3efe6;
    --label-paper: #ead9b4;
    --label-edge: #cdb88c;
    --money-light: #dfe3d8;
    --money-mid: #a9b1a0;
    --money-dark: #6e7666;
  }
  html, body {
    margin: 0;
    padding: 0;
    overflow: hidden;
    background: #ffffff;
  }
  .cover {
    position: relative;
    width: 750px;
    height: 1200px;
    overflow: hidden;
    background-color: var(--door-orange);
    background-image: repeating-linear-gradient(
      to bottom,
      var(--door-light) 0px,
      var(--door-orange) 14px,
      var(--door-orange) 44px,
      var(--door-shadow) 52px,
      var(--door-deep) 55px,
      var(--door-light) 58px
    );
  }
  .author {
    position: absolute;
    top: 118px;
    left: 0;
    width: 100%;
    margin: 0;
    text-align: center;
    font-family: "Archivo Black", sans-serif;
    font-size: 50px;
    letter-spacing: 5px;
    color: var(--ink);
    line-height: 1;
  }
  .title {
    position: absolute;
    top: 222px;
    left: 0;
    width: 100%;
    margin: 0;
    text-align: center;
    font-family: "Anton", sans-serif;
    font-weight: 400;
    color: var(--title-white);
    text-shadow: 0 3px 0 rgba(120, 60, 15, 0.35);
  }
  .title-lead {
    display: block;
    font-size: 88px;
    line-height: 96px;
    letter-spacing: 2px;
  }
  .title-main {
    display: block;
    font-size: 164px;
    line-height: 150px;
    letter-spacing: 4px;
    transform: scaleX(1.08);
  }
  .money-pile {
    position: absolute;
    left: 0;
    top: 765px;
    width: 750px;
    height: 435px;
  }
  .subtitle-label {
    position: absolute;
    left: -6px;
    top: 938px;
    width: 746px;
    height: 140px;
    background: var(--label-paper);
    border-bottom: 3px solid var(--label-edge);
    box-shadow: 0 4px 8px rgba(0, 0, 0, 0.25);
    display: flex;
    flex-direction: column;
    justify-content: center;
    align-items: center;
  }
  .subtitle-label p {
    margin: 0;
    font-family: "Fjalla One", sans-serif;
    font-size: 40px;
    line-height: 52px;
    color: var(--ink);
    white-space: nowrap;
  }
</style>
</head>
<body>
  <main class="cover">
    <p class="author">DALTON MERRIWEATHER</p>
    <h1 class="title">
      <span class="title-lead">MAKING MONEY IN</span>
      <span class="title-main">STORAGE</span>
      <span class="title-main">AUCTIONS</span>
    </h1>
    <svg class="money-pile" viewBox="0 0 750 435" role="img" aria-label="Photograph of a heaped pile of hundred-dollar bills">
      <defs>
        <linearGradient id="money-tone" x1="0" y1="0" x2="0" y2="1">
          <stop offset="0" stop-color="var(--money-light)"/>
          <stop offset="0.5" stop-color="var(--money-mid)"/>
          <stop offset="1" stop-color="var(--money-dark)"/>
        </linearGradient>
      </defs>
      <path d="M0 110 L80 95 L180 70 L260 50 L330 20 L380 8 L430 25 L520 45 L600 70 L680 100 L750 125 L750 435 L0 435 Z" fill="url(#money-tone)"/>
    </svg>
    <div class="subtitle-label">
      <p>How to Profit from the Locker Raiders</p>
      <p>&amp; Become A Storage Auction Warrior</p>
    </div>
  </main>
</body>
</html>
```